Crestwell Renewal Business Card Design Phase 2

Professional and clean design. The design colors should flow with the logo. Two-sided card with the website on the back which is:

www.CrestwellRenewal.example.

"Specializing in Water Damage Restoration"

On the front I need the name, email, phone, and logo.

Name: Dorian Halvek
Email: Dorian@CrestwellRenewal.example
Phone: 555-318-2046 for now

I only have the Preview and Thumbnail right now but should have the source files uploaded within a day or two.

Target Market(s)

Flood victims, home owners with water damage from busted pipes etc...

Industry/Entity Type

Business

Contact Information for Business Card

Name: Dorian Halvek

Font styles to use
Serif
Sans Serif

Requirements
Must have
• Business Card Details Info

```html
<!DOCTYPE html>
<html lang="en">
<head>
<meta charset="utf-8">
<title>Crestwell Renewal Business Card</title>
<link href="https://fonts.googleapis.com/css2?family=Oswald:wght@500&family=Open+Sans:wght@400;600&display=swap" rel="stylesheet">
<style>
  :root {
    --navy: #1f3a63;
    --navy-shade: #1a3256;
    --green: #4f9140;
    --ink: #2f3338;
    --rule: #c9c9c9;
    --paper: #ffffff;
    --ghost: #f3f3f1;
    --backdrop: #e8e5e1;
  }
  * { margin: 0; padding: 0; box-sizing: border-box; }
  html, body {
    width: 1200px; height: 1000px; overflow: hidden;
    background: var(--backdrop);
    font-family: "Open Sans", Arial, sans-serif;
  }
  .card {
    position: absolute; left: 265px; width: 666px; height: 398px;
    overflow: hidden;
    box-shadow: 0 4px 12px rgba(0,0,0,0.18);
  }
  .card--front { top: 73px; background: var(--paper); }
  .card--back { top: 532px; background: var(--navy); }

  .brand-name {
    position: absolute; left: 32px; top: 24px;
    font-family: "Oswald", "Arial Narrow", sans-serif;
    font-weight: 500; font-size: 62px; line-height: 62px;
    letter-spacing: 0.5px; text-transform: uppercase;
  }
  .card--front .brand-name { color: var(--navy); }
  .card--back .brand-name { color: var(--paper); top: 28px; }

  .decoration {
    position: absolute; border-radius: 6px;
  }
  .card--front .decoration {
    left: 240px; top: 100px; width: 420px; height: 280px;
    background: radial-gradient(ellipse at 60% 50%, var(--ghost) 0%, rgba(243,243,241,0) 75%);
  }
  .card--back .decoration {
    left: 220px; top: 70px; width: 440px; height: 320px;
    background: radial-gradient(ellipse at 60% 55%, var(--navy-shade) 0%, rgba(26,50,86,0) 75%);
  }

  .divider {
    position: absolute; left: 32px; top: 237px; width: 410px; height: 2px;
    background: var(--rule);
  }
  .holder-name {
    position: absolute; left: 453px; top: 224px;
    font-weight: 600; font-size: 20px; color: var(--navy);
  }
  .contact-list {
    position: absolute; left: 32px; top: 268px; list-style: none;
  }
  .contact-item {
    display: flex; align-items: center; gap: 7px;
    font-size: 16px; line-height: 26px; color: var(--ink);
  }
  .contact-icon { width: 15px; height: 15px; fill: var(--navy); }

  .footer-band { position: absolute; left: 0; bottom: 0; width: 666px; height: 26px; }
</style>
</head>
<body>

<section class="card card--front" aria-label="Card front">
  <div class="decoration" role="img" aria-label="Faint background illustration of a flooded house and a restoration worker"></div>
  <div class="brand-name">Crestwell<br>Renewal</div>
  <div class="divider"></div>
  <div class="holder-name">Dorian Halvek</div>
  <ul class="contact-list">
    <li class="contact-item">
      <svg class="contact-icon" viewBox="0 0 16 16"><path d="M1 5c0-2 3-3 7-3s7 1 7 3v1h-4V4.5H5V6H1z"/><path d="M3 7h10l1 7H2z"/></svg>
      555-318-2046
    </li>
    <li class="contact-item">
      <svg class="contact-icon" viewBox="0 0 16 16"><path d="M1 3h14v10H1z"/><path d="M1.5 3.5 8 9l6.5-5.5" fill="none" stroke="#fff" stroke-width="1.4"/></svg>
      Dorian@CrestwellRenewal.example
    </li>
    <li class="contact-item">
      <svg class="contact-icon" viewBox="0 0 16 16"><circle cx="8" cy="8" r="7"/><path d="M1 8h14M8 1c-3 3-3 11 0 14M8 1c3 3 3 11 0 14" fill="none" stroke="#fff" stroke-width="1"/></svg>
      www.CrestwellRenewal.example
    </li>
  </ul>
  <svg class="footer-band" viewBox="0 0 666 26" preserveAspectRatio="none">
    <polygon points="0,0 392,0 365,26 0,26" fill="var(--green)"/>
    <polygon points="398,0 666,0 666,26 371,26" fill="var(--navy)"/>
  </svg>
</section>

<section class="card card--back" aria-label="Card back">
  <div class="decoration" role="img" aria-label="Faint background illustration of a flooded house and a restoration worker"></div>
  <div class="brand-name">Crestwell<br>Renewal</div>
</section>

</body>
</html>
```